LUMAGRID Carrying Insight Across The Digital Frontier\Government Contracting IT, Software, Networks

We need a business card design for a new Government Joint Venture based out of Omaha, NE. We provide all types of technology needs to all types of Government agencies. I have attached logo and capability statement to identify our companies industry and offerings. extremely import information that needs to be identified on the cards is SBA: 8(a), SBA: SDB, SBA: HUBZone

Target Market(s)

Government Contracting Officers

Industry/Entity Type

Business

Contact Information for Business Card

Glen Harwick
Vice President
7182 N 41st Avenue
Omaha, NE 68219
P: 402-563-2174
F: 402-563-2175
Toll: 855-614-3920
glen@lumagrid.example
http://www.lumagrid.example
Dario Quenell
President
7182 N 41st Avenue
Omaha, NE 68219
P: 402-563-2174
F: 402-563-2175
Toll: 855-614-3920
dario@lumagrid.example
http://www.lumagrid.example

Number of Pages Required

4 page

Font styles to use
Serif

Requirements
Must have
• Look and feel should be technical.

```html
<!DOCTYPE html>
<html lang="en">
<head>
<meta charset="utf-8">
<title>LUMAGRID — Business Card</title>
<link rel="stylesheet" href="https://fonts.googleapis.com/css2?family=Saira+Condensed:wght@400;500;700&display=swap">
<style>
  :root {
    --brand-violet: #4229bb;
    --card-bg: #f8f8fa;
    --panel-text: #ffffff;
    --brand-ink: #3a1fb0;
  }
  * { margin: 0; padding: 0; box-sizing: border-box; }
  html, body { width: 1200px; height: 667px; overflow: hidden; background: var(--card-bg); }
  .card {
    position: relative;
    width: 1200px;
    height: 667px;
    background: var(--card-bg);
    font-family: "Saira Condensed", "Arial Narrow", sans-serif;
  }
  .brand {
    position: absolute;
    left: 100px;
    top: 140px;
    width: 380px;
    text-align: center;
  }
  .brand-mark {
    display: block;
    width: 236px;
    height: 236px;
    margin: 0 auto;
    border-radius: 50%;
    background: var(--brand-violet);
  }
  .brand-name {
    margin-top: 30px;
    font-size: 74px;
    font-weight: 500;
    letter-spacing: 3px;
    line-height: 1;
    color: var(--brand-ink);
  }
  .contact-panel {
    position: absolute;
    left: 583px;
    top: 81px;
    width: 617px;
    height: 486px;
    background: var(--brand-violet);
    border-radius: 24px 0 0 24px;
    color: var(--panel-text);
    padding: 38px 0 0 56px;
  }
  .person-name {
    font-size: 42px;
    font-weight: 700;
    letter-spacing: 1.5px;
    line-height: 1;
  }
  .person-title {
    margin-top: 22px;
    font-size: 30px;
    font-weight: 400;
    letter-spacing: 1.5px;
    line-height: 1;
  }
  .address {
    margin-top: 44px;
    font-size: 30px;
    letter-spacing: 1.5px;
    line-height: 1;
  }
  .contact-list {
    list-style: none;
    margin-top: 38px;
  }
  .contact-item {
    display: flex;
    align-items: center;
    height: 47px;
    font-size: 30px;
    letter-spacing: 1.5px;
  }
  .contact-icon {
    width: 26px;
    height: 22px;
    margin-right: 29px;
    fill: var(--panel-text);
  }
  .contact-note { margin-left: 14px; }
  .certifications {
    position: absolute;
    left: 693px;
    top: 586px;
    font-size: 26px;
    letter-spacing: 1px;
    color: var(--brand-violet);
    line-height: 1;
  }
</style>
</head>
<body>
<main class="card">
  <section class="brand">
    <span class="brand-mark" aria-hidden="true"></span>
    <div class="brand-name">LUMAGRID</div>
  </section>

  <section class="contact-panel">
    <h1 class="person-name">Dario Quenell</h1>
    <p class="person-title">President</p>
    <p class="address">7182 N 41st Avenue Omaha, NE 68219</p>
    <ul class="contact-list">
      <li class="contact-item">
        <svg class="contact-icon" viewBox="0 0 26 22" aria-label="Phone"><path d="M2 8 C2 3 24 3 24 8 L24 10 L18 10 L18 7 L8 7 L8 10 L2 10 Z M8 11 L18 11 L23 20 L3 20 Z M13 13 A3 3 0 1 0 13.01 13 Z" fill-rule="evenodd"/></svg>
        402-563-2174
      </li>
      <li class="contact-item">
        <svg class="contact-icon" viewBox="0 0 26 22" aria-label="Fax"><path d="M6 1 H20 V7 H6 Z M1 8 H25 V17 H21 V13 H5 V17 H1 Z M6 14 H20 V21 H6 Z M8 16 V17 H18 V16 Z M8 18 V19 H18 V18 Z" fill-rule="evenodd"/></svg>
        402-563-2175
      </li>
      <li class="contact-item">
        <svg class="contact-icon" viewBox="0 0 26 22" aria-label="Toll free phone"><path d="M2 8 C2 3 24 3 24 8 L24 10 L18 10 L18 7 L8 7 L8 10 L2 10 Z M8 11 L18 11 L23 20 L3 20 Z M13 13 A3 3 0 1 0 13.01 13 Z" fill-rule="evenodd"/></svg>
        855-614-3920<span class="contact-note">Toll Free</span>
      </li>
      <li class="contact-item">
        <svg class="contact-icon" viewBox="0 0 26 22" aria-label="Email"><path d="M1 3 H25 V19 H1 Z M3 5 V6 L13 13 L23 6 V5 Z M3 8.5 V17 H23 V8.5 L13 15.5 Z" fill-rule="evenodd"/></svg>
        dario@lumagrid.example
      </li>
    </ul>
  </section>

  <p class="certifications">SBA: 8(a), SBA: SDB, SBA: HUBZone</p>
</main>
</body>
</html>
```